New business card for my lawn and landscape business

Dorrin Yard and Building is a full-service lawn care, landscaping, and light construction company serving Paragould and the Northeast Arkansas region. The business is owned and operated by Marcus Toller, with a reputation for hands-on, detail-oriented service, dependable crews, and quality results for both residential and commercial clients. A well regarded business with great reviews.
Owner Marcus Toller
Dorrinyardandbuilding.example

Target Market(s)

Commercial, Middle, and upper class in north east Arkansas

Industry/Entity Type

Lawn maintenance and landscape

Contact Information for Business Card

Dorrin Yard And Building Professional lawn care, landscaping, and property improvement in Northeast Arkansas. • lawn maintenance •lawn treatments and weed control • exterior projects • Custom landscape design & installation • Sod, trees, rock & drainage solutions • Residential & commercial services Reliable. Detailed. Done right.

Requirements
Must have
• Business name, service area, list of some of our services, clean design that represents
Nice to have
• Unique. Different design element than just grass because its already in n the logo. Picture of a warm season (south) lawn or landscape. Pictures of the type of work we do

```html
<!DOCTYPE html>
<html lang="en">
<head>
<meta charset="utf-8">
<title>Dorrin Yard And Building – Business Card</title>
<link rel="stylesheet" href="https://fonts.googleapis.com/css2?family=Montserrat:wght@400;600&display=swap">
<style>
  :root {
    --stage: #d3d3d3;
    --paper: #ffffff;
    --leaf: #7aae41;
    --slate: #878787;
    --ink-light: #ffffff;
    --ring: #8c8c8c;
  }
  * { margin: 0; padding: 0; box-sizing: border-box; }
  html, body {
    width: 1200px;
    height: 1200px;
    overflow: hidden;
    background: var(--stage);
    font-family: "Montserrat", sans-serif;
  }
  .canvas {
    position: relative;
    width: 1200px;
    height: 1200px;
  }
  .card {
    position: absolute;
    left: 169px;
    width: 864px;
    height: 505px;
    background: var(--paper);
    overflow: hidden;
  }
  .card--front { top: 78px; }
  .card--back { top: 617px; }
  .card__shapes {
    position: absolute;
    inset: 0;
    width: 100%;
    height: 100%;
  }
  .shape--slate { fill: var(--slate); }
  .shape--leaf { fill: var(--leaf); }
  .shape--emblem { fill: var(--paper); stroke: var(--ring); stroke-width: 1.6; }

  .intro {
    position: absolute;
    left: 56px;
    top: 72px;
    width: 440px;
    color: var(--ink-light);
    font-size: 18px;
    line-height: 24px;
    font-weight: 400;
  }
  .services {
    position: absolute;
    left: 56px;
    top: 288px;
    list-style: none;
    color: var(--ink-light);
    font-size: 19px;
    line-height: 30px;
    font-weight: 400;
  }
  .services li::before {
    content: "·";
    margin-right: 6px;
  }

  .brand {
    position: absolute;
    display: flex;
    align-items: center;
    gap: 14px;
  }
  .brand--front {
    left: 540px;
    top: 222px;
  }
  .brand__dot {
    flex: none;
    width: 52px;
    height: 52px;
    border-radius: 50%;
    border: 3px solid var(--ring);
  }
  .brand__name {
    color: var(--leaf);
    font-weight: 600;
    font-size: 25px;
    line-height: 30px;
  }
  .brand--back {
    left: 96px;
    top: 196px;
    width: 358px;
    justify-content: center;
    text-align: center;
  }
  .brand--back .brand__name {
    font-size: 30px;
    line-height: 36px;
  }
</style>
</head>
<body>
<main class="canvas">

  <section class="card card--front" aria-label="Business card front">
    <svg class="card__shapes" viewBox="0 0 691 404" preserveAspectRatio="none" aria-hidden="true">
      <polygon class="shape--slate" points="13,0 440,0 372,200 386,228 13,148"/>
      <polygon class="shape--leaf" points="0,153 386,238 465,404 0,404"/>
      <polygon class="shape--leaf" points="460,0 485,0 400,203 420,232 405,232 378,203"/>
    </svg>

    <p class="intro">Dorrin Yard And Building Professional lawn care, landscaping, and property improvement in Northeast Arkansas.</p>

    <ul class="services">
      <li>Lawn maintenance</li>
      <li>Lawn treatments and weed control</li>
      <li>Exterior projects</li>
      <li>Custom landscape design &amp; installation</li>
      <li>Sod, trees, rock &amp; drainage solutions</li>
      <li>Residential &amp; commercial services Reliable</li>
    </ul>

    <div class="brand brand--front">
      <span class="brand__dot" aria-hidden="true"></span>
      <span class="brand__name">Dorrin Yard<br>&amp; Building LLC</span>
    </div>
  </section>

  <section class="card card--back" aria-label="Business card back">
    <svg class="card__shapes" viewBox="0 0 691 404" preserveAspectRatio="none" aria-hidden="true">
      <path class="shape--leaf" d="M245,0 L691,0 Q690,340 345,404 C445,330 420,70 245,0 Z"/>
      <circle class="shape--emblem" cx="220" cy="201" r="143"/>
    </svg>

    <div class="brand brand--back">
      <span class="brand__name">Dorrin Yard<br>&amp; Building LLC</span>
    </div>
  </section>

</main>
</body>
</html>
```